Velmont Chamber of Commerce Website

We have been asked to design a new website for the Velmont Chamber of Commerce. The mission of the Greater Velmont Chamber of Commerce is to develop and promote an economically vibrant business community aggressively. The website should reflect a modern, professional design that showcases local businesses and promotes the programs the Chamber has to offer.

```html
<!DOCTYPE html>
<html lang="en">
<head>
<meta charset="utf-8">
<title>Greater Velmont Chamber of Commerce</title>
<link rel="stylesheet" href="https://fonts.googleapis.com/css2?family=Roboto:wght@300;400;500;700&family=Roboto+Condensed:wght@700&display=swap">
<style>
:root{
  --topbar:#1f1f1f;
  --topbar-light:#d6d6d6;
  --topbar-link:#b5b5b5;
  --header-bg:#f2f2f2;
  --navy:#1d3f73;
  --brand-blue:#3a65ac;
  --brand-blue-dark:#2f5594;
  --ink:#222222;
  --muted:#5f6368;
  --required:#e0393e;
  --modal-bg:#eceef1;
  --field:#ffffff;
  --field-border:#d0d4da;
  --button:#242424;
  --dim:rgba(20,24,30,0.16);
}
*{box-sizing:border-box;margin:0;padding:0}
html,body{width:1200px;height:703px;overflow:hidden}
body{position:relative;font-family:"Roboto",Arial,sans-serif;color:var(--ink);background:var(--header-bg)}

/* top bar */
.topbar{position:absolute;left:0;top:0;width:1200px;height:28px;background:var(--topbar)}
.topbar-social-zone{position:absolute;left:0;top:0;height:28px;width:248px;background:var(--topbar-light);clip-path:polygon(0 0,215px 0,248px 28px,0 28px)}
.social{position:absolute;top:7px;width:14px;height:14px;border-radius:50%;background:#2b2b2b}
.toplinks{position:absolute;right:44px;top:0;height:28px;display:flex;align-items:center;font-size:10px;color:var(--topbar-link)}
.toplinks span{padding:0 9px;border-left:1px solid #444}
.toplinks span:first-child{border-left:none}
.toplinks span:last-child{padding-right:0}

/* header */
.header{position:absolute;left:0;top:28px;width:1200px;height:92px;background:var(--header-bg)}
.brand{position:absolute;left:44px;top:16px;display:flex;align-items:center;gap:8px}
.brand-dot{width:36px;height:36px;border-radius:50%;background:var(--navy)}
.brand-name{font-weight:700;font-size:10px;line-height:11px;color:var(--navy);text-transform:uppercase;width:96px}
.contact{position:absolute;left:842px;top:22px;font-size:13px;font-weight:500}
.contact small{display:block;font-size:9px;font-weight:400;color:#666;margin-top:3px}
.header-cta{position:absolute;left:1009px;top:20px;width:146px;height:31px;background:var(--brand-blue);color:#fff;font-size:11.5px;display:flex;align-items:center;justify-content:center;border-radius:2px}

/* hero */
.hero{position:absolute;left:0;top:120px;width:1200px;height:583px;background:linear-gradient(180deg,#5f86b6 0%,#8fa9c6 35%,#b0bac4 55%,#5d6f86 72%,#2f4660 100%)}
.nav{position:absolute;left:44px;top:98px;width:1112px;height:44px;background:var(--brand-blue);border-radius:3px 3px 0 0;z-index:2}
.nav a{position:absolute;top:0;height:44px;line-height:44px;color:#e4ebf6;font-size:12.5px;text-decoration:none}
.nav a.active{font-weight:700;color:#fff}
.nav a.active::after{content:"";position:absolute;left:0;right:0;bottom:0;height:3px;background:#e9eef7}
.nav-search{position:absolute;right:0;top:0;width:44px;height:44px;background:var(--brand-blue-dark);display:flex;align-items:center;justify-content:center}
.hero-title{position:absolute;left:0;top:303px;width:1200px;text-align:center;font-family:"Roboto Condensed",Arial,sans-serif;font-weight:700;font-size:60px;color:#d9d9d9}
.hero-sub{position:absolute;left:0;top:406px;width:1200px;text-align:center;font-size:26px;color:#e4e6ea;font-weight:300}
.band{position:absolute;left:0;top:647px;width:1200px;height:56px;background:#e9e9e9}
.card{position:absolute;top:606px;width:192px;height:110px;background:#f1f1f1;padding:4px}
.card-photo{width:100%;height:100%;background:linear-gradient(160deg,#9b9894,#5f5a57 60%,#3e3d40)}

.overlay{position:absolute;inset:0;background:var(--dim);z-index:5}

/* modal */
.modal{position:absolute;left:358px;top:40px;width:484px;height:623px;border-radius:10px;background:linear-gradient(180deg,#f3f4f6 0%,var(--modal-bg) 100%);box-shadow:0 8px 30px rgba(0,0,0,.18);z-index:10}
.modal-close{position:absolute;left:449px;top:17px}
.modal h2{position:absolute;left:44px;top:52px;font-family:"Roboto Condensed",Arial,sans-serif;font-size:21px;line-height:26px;color:var(--ink)}
.modal-intro{position:absolute;left:44px;top:91px;width:400px;font-size:14.5px;line-height:21px}
.field-label{position:absolute;left:44px;font-size:14.5px;font-weight:500}
.field-label em{color:var(--required);font-style:normal}
.field{position:absolute;left:44px;width:395px;height:37px;background:var(--field);border:1px solid var(--field-border);border-radius:3px}
.legal{position:absolute;left:44px;top:413px;width:400px;font-size:11.4px;line-height:15.8px;color:var(--muted)}
.legal u{color:#4a4d52;font-weight:500}
.submit{position:absolute;left:44px;top:535px;width:395px;height:44px;background:var(--button);color:#fff;font-size:14.5px;font-weight:500;border-radius:3px;display:flex;align-items:center;justify-content:center}
</style>
</head>
<body>

<div class="topbar">
  <div class="topbar-social-zone">
    <span class="social" style="left:44px"></span>
    <span class="social" style="left:69px"></span>
    <span class="social" style="left:93px"></span>
    <span class="social" style="left:118px"></span>
    <span class="social" style="left:142px"></span>
  </div>
  <nav class="toplinks">
    <span>Economic Update</span><span>Join Our Email List</span><span>Community Info</span><span>Resources + Links</span>
  </nav>
</div>

<header class="header">
  <div class="brand">
    <span class="brand-dot"></span>
    <span class="brand-name">Greater Velmont Chamber of Commerce</span>
  </div>
  <div class="contact">info@visitvelmont.org<small>Contact us now !</small></div>
  <div class="header-cta">Join Our Mailing List!</div>
</header>

<section class="hero" role="img" aria-label="Riverfront photo with a footbridge, waterside buildings and calm water under a blue sky"></section>

<nav class="nav">
  <a class="active" style="left:35px">Home</a>
  <a style="left:98px">Business Resources</a>
  <a style="left:238px">Programs</a>
  <div class="nav-search">
    <svg width="20" height="20" viewBox="0 0 20 20" fill="none" stroke="#cfdcf0" stroke-width="1.6"><circle cx="9" cy="9" r="7"/><line x1="14" y1="14" x2="19" y2="19"/></svg>
  </div>
</nav>

<div class="hero-title">Move Business Forward</div>
<div class="hero-sub">Join the largest business network in Velmont.</div>

<div class="band"></div>
<div class="card" style="left:90px"><div class="card-photo" role="img" aria-label="Group photo of chamber members holding certificates"></div></div>
<div class="card" style="left:297px"><div class="card-photo" role="img" aria-label="Ribbon cutting ceremony"></div></div>
<div class="card" style="left:504px"><div class="card-photo" role="img" aria-label="Members gathered at a chamber event"></div></div>
<div class="card" style="left:711px"><div class="card-photo" role="img" aria-label="Networking meeting at a local business"></div></div>
<div class="card" style="left:920px"><div class="card-photo" role="img" aria-label="Award presentation between two members"></div></div>

<div class="overlay"></div>

<div class="modal" role="dialog" aria-label="Join Our Mailing List">
  <svg class="modal-close" width="16" height="16" viewBox="0 0 16 16" stroke="#555" stroke-width="1.6"><line x1="2" y1="2" x2="14" y2="14"/><line x1="14" y1="2" x2="2" y2="14"/></svg>
  <h2>Join Our Mailing List!</h2>
  <p class="modal-intro">By signing up, you’ll be the first to hear about Chamber News and Events, Community Events, exciting Offers, and MORE!</p>

  <div class="field-label" style="top:147px">Email<em>*</em></div>
  <div class="field" style="top:179px"></div>
  <div class="field-label" style="top:236px">First Name<em>*</em></div>
  <div class="field" style="top:267px"></div>
  <div class="field-label" style="top:325px">Last Name<em>*</em></div>
  <div class="field" style="top:356px"></div>

  <p class="legal">By submitting this form, you are consenting to receive marketing emails from: Velmont Chamber of Commerce, 210 N. Harbor Avenue Ste. 120, Velmont , CA, 95099 United States. You can revoke your consent to receive emails at any time by using the EasyOptOut EasyOptOut® link, found at the bottom of every email. <u>Emails are serviced by MailRiver</u>.</p>

  <div class="submit">Sign Up Now</div>
</div>

</body>
</html>
```